Tallow Creek Biotics - Business Card Design

Business Card Brief;
We require a design for a business card template for our business “Tallow Creek Biotics”.
We are a firm that manufacture positive microbial formulations to enhance agricultural legume crops such as lucence, soy beans and faba beans. We also manufacture microbial formulations that aid in composting of waste organic waste to use as a natural fertilizer.
We are seeking a business card design that portrays a clean, professional organisation dedicated to enhancing nature and sustainable farming techniques.
Our website is www.soilvantage.com.au
Here is a link to a drawing of a soybean plant. One of our main products is used to help grow these. I offer it an an example of the type of graphic that might be used on the card, but will leave you to create your own design; https://pixelvaultimages.com/482915066/stock-illustration-soybean-plant-on-a-white.html
Two cards are required;
--------------------------------------------------------------------
Card #1
Cody R Whitfield
Executive Chairman
Mobile: 0471 583204
Email: cody@soilvantage.com.au
---------------------------------------------------------------------------
Card #2
Lachlan P Doyce
Chief Financial & Operating Officer
Mobile: 0456 792418
Email lachlan@soilvantage.com.au

Many thanks
Lachlan Doyce

Industry/Entity Type

Agriculture

Colors

Designer to choose colors to be used in the design.

Requirements
Must have
• An elegant design that demonstrates our commitment to enhancing nature.

```html
<!DOCTYPE html>
<html lang="en">
<head>
<meta charset="utf-8">
<title>Tallow Creek Biotics – Business Card</title>
<link href="https://fonts.googleapis.com/css2?family=Open+Sans:wght@300;400;700&display=swap" rel="stylesheet">
<style>
  :root {
    --page-bg: #e9ecef;
    --card-light: #2fb6f2;
    --card-mid: #1a98e6;
    --card-deep: #0d56c4;
    --ink-white: #ffffff;
    --ink-soft: rgba(255, 255, 255, 0.92);
  }
  * { margin: 0; padding: 0; box-sizing: border-box; }
  html, body {
    width: 1200px;
    height: 800px;
    overflow: hidden;
    background: var(--page-bg);
  }
  .stage {
    width: 1200px;
    height: 800px;
    display: flex;
    align-items: center;
    justify-content: center;
  }
  .business-card {
    position: relative;
    width: 960px;
    height: 585px;
    overflow: hidden;
    font-family: "Open Sans", Arial, sans-serif;
    color: var(--ink-white);
    background:
      radial-gradient(ellipse 38% 30% at 45% 42%, rgba(13, 86, 196, 0.75), rgba(13, 86, 196, 0) 70%),
      radial-gradient(ellipse 30% 22% at 30% 70%, rgba(20, 110, 210, 0.45), rgba(20, 110, 210, 0) 70%),
      radial-gradient(ellipse 45% 40% at 85% 80%, rgba(70, 210, 255, 0.5), rgba(70, 210, 255, 0) 70%),
      linear-gradient(135deg, var(--card-light) 0%, var(--card-mid) 50%, var(--card-light) 100%);
    box-shadow: 0 6px 18px rgba(0, 0, 0, 0.18);
  }
  .brand {
    position: absolute;
    top: 92px;
    left: 560px;
    display: flex;
    align-items: center;
    gap: 22px;
  }
  .brand-dot {
    width: 64px;
    height: 64px;
    border-radius: 50%;
    background: rgba(255, 255, 255, 0.85);
    flex-shrink: 0;
  }
  .brand-name {
    font-weight: 400;
    font-size: 44px;
    line-height: 1.02;
    color: var(--ink-white);
  }
  .contact-block {
    position: absolute;
    left: 160px;
    top: 352px;
  }
  .person-name {
    font-weight: 300;
    font-size: 48px;
    line-height: 1;
    letter-spacing: 0.5px;
  }
  .person-title {
    margin-top: 6px;
    font-weight: 700;
    font-size: 11px;
    letter-spacing: 2.2px;
    text-transform: uppercase;
  }
  .contact-list {
    margin-top: 26px;
    list-style: none;
    font-weight: 700;
    font-size: 19px;
    line-height: 1.35;
    letter-spacing: 1.6px;
    color: var(--ink-soft);
  }
  .contact-list li { display: flex; }
  .contact-label {
    width: 44px;
    font-size: 14px;
    padding-top: 3px;
  }
</style>
</head>
<body>
  <main class="stage">
    <article class="business-card">
      <header class="brand">
        <span class="brand-dot"></span>
        <span class="brand-name">Tallow Creek<br>Biotics</span>
      </header>
      <section class="contact-block">
        <h1 class="person-name">Lachlan P Doyce</h1>
        <p class="person-title">Chief Financial &amp; Operating Officer</p>
        <ul class="contact-list">
          <li><span class="contact-label">M:</span>0456 792418</li>
          <li><span class="contact-label">E:</span>lachlan@soilvantage.com.au</li>
          <li><span class="contact-label">W:</span>www.soilvantage.com.au</li>
        </ul>
      </section>
    </article>
  </main>
</body>
</html>
```